Buch-Cover für Schweden-Krimi
Eine wirklich wunderbare Zusammenarbeit! Schon der erste Entwurf von ihr hat mir richtig gut gefallen; anschließende Anregungen wurden sehr schnell und äußerst professionell umgesetzt. Moonwhale kann daher uneingeschränkt empfohlen werden!
Zielgruppe
Ich bin ein Krimi-Autor. Die Zielgruppe liest gerne Krimis (oder auch Thriller) und hat eine Vorliebe für den Norden / Skandinavien.
Aufgabenstellung
Der Schweden-Krimi mit dem Titel 'Wo Schatten ruhen. Inspektor Malmgrens letzter Tag' spielt in Värmland, eine recht einsame Gegend mit vielen Seen und viel Wald. Zwei junge Frauen, die auch der Suche nach Freiheit waren, werden auf einer kleinen Insel in einem See tot aufgefunden. Ihre Leichen wurden vergraben, doch so drapiert, dass von einer die Hand aus dem Erdreich schaut, die geöffnete Handfläche nach oben. Dieses Bild könnte sich gut auf dem Cover machen. Auch mit den Elementen See, Wald, Licht und Dunkel kann gespielt werden.
'Wo Schatten ruhen' ist der Haupttitel, der dementsprechend groß gedruckt werden sollte. Der Untertitel 'Inspektor Malmgrens letzter Tag' kann kleiner abgedruckt werden, ebenso die Genre-Bezeichnung 'Krimi' bzw. 'Kriminalroman'.
E-Book: Maße 1,6 : 1 (idealerweise 2560 x 1600 px)
Buch: 12,7 x 20,32 cm (Buchdicke steht noch nicht endgültig fest)

```html
<!DOCTYPE html>
<html lang="de">
<head>
<meta charset="utf-8">
<title>Wo Schatten ruhen – Buchumschlag</title>
<link rel="stylesheet" href="https://fonts.googleapis.com/css2?family=Barlow+Condensed:wght@500;600;700&family=Kaushan+Script&family=Roboto+Condensed:wght@400&display=swap">
<style>
  :root {
    --stage: #3a2a1e;
    --night: #131518;
    --mist: #b4b8a8;
    --sky-light: #dfe2d3;
    --sky-mid: #9fa595;
    --hill: #3b403a;
    --forest: #262a25;
    --title-grey: #d2d2cd;
    --author-grey: #3a3d3f;
    --signal-red: #d9151b;
    --paper-white: #ecebe6;
  }
  * { margin: 0; padding: 0; box-sizing: border-box; }
  html, body { width: 1200px; height: 800px; overflow: hidden; }
  body {
    background: radial-gradient(ellipse 70% 60% at 50% 40%, #5a3f28, var(--stage) 70%, #24190f 100%);
    display: flex;
    align-items: center;
    justify-content: center;
  }
  .cover-wrap {
    display: flex;
    height: 680px;
    box-shadow: 0 14px 36px rgba(0,0,0,.55);
  }
  .panel { position: relative; height: 100%; overflow: hidden; }
  .back-cover, .front-cover { width: 425px; }
  .spine { width: 30px; background: linear-gradient(90deg, #0d0e10, var(--night) 40%, #1c1e21); }

  .scene-art { position: absolute; inset: 0; }

  .front-cover .scene-art {
    background:
      radial-gradient(ellipse 22% 12% at 66% 9%, rgba(248,249,242,.95), transparent 75%),
      radial-gradient(ellipse 30% 40% at 92% 30%, rgba(30,34,30,.55), transparent 70%),
      radial-gradient(ellipse 18% 8% at 22% 30%, rgba(240,242,232,.55), transparent 75%),
      radial-gradient(ellipse 60% 10% at 45% 47%, rgba(150,156,140,.55), transparent 80%),
      radial-gradient(ellipse 40% 12% at 68% 60%, rgba(120,126,112,.45), transparent 80%),
      radial-gradient(ellipse 22% 8% at 55% 78%, rgba(140,142,128,.40), transparent 80%),
      linear-gradient(180deg,
        var(--sky-light) 0%, var(--mist) 18%, var(--sky-mid) 30%,
        #6a7064 36%, var(--hill) 42%, #4a5046 50%,
        #353a33 58%, var(--forest) 68%, #1d201c 82%, var(--night) 100%);
    box-shadow: inset 0 0 90px rgba(0,0,0,.55);
  }
  .back-cover .scene-art {
    background:
      radial-gradient(ellipse 20% 9% at 42% 8%, rgba(246,247,240,.9), transparent 75%),
      radial-gradient(ellipse 16% 8% at 18% 12%, rgba(230,232,222,.55), transparent 75%),
      radial-gradient(ellipse 75% 32% at 50% 18%, rgba(176,180,164,.85), transparent 78%),
      radial-gradient(ellipse 32% 14% at 82% 52%, rgba(120,126,118,.5), transparent 78%),
      radial-gradient(ellipse 30% 8% at 70% 68%, rgba(90,94,86,.5), transparent 80%),
      linear-gradient(180deg, #474b43 0%, #3a3e37 30%, #2f332d 45%, #252823 62%, #1b1d1b 80%, var(--night) 100%);
    box-shadow: inset 0 0 110px rgba(0,0,0,.7);
  }

  .author {
    position: absolute; left: 0; right: 0; top: 56px;
    text-align: center;
    font-family: "Barlow Condensed", sans-serif;
    font-weight: 600;
    font-size: 27px;
    letter-spacing: .5px;
    color: var(--author-grey);
  }
  .title-block {
    position: absolute; left: 0; right: 0; top: 232px;
    text-align: center;
  }
  .title-lead, .title-main, .title-tail { display: block; }
  .title-lead {
    font-family: "Barlow Condensed", sans-serif;
    font-weight: 700;
    font-size: 62px;
    line-height: 1;
    color: var(--signal-red);
    position: relative; z-index: 0;
  }
  .title-main {
    font-family: "Kaushan Script", cursive;
    font-weight: 400;
    font-size: 88px;
    line-height: .9;
    color: var(--title-grey);
    margin-top: -22px;
    position: relative; z-index: 1;
    text-shadow: 0 2px 6px rgba(0,0,0,.35);
  }
  .title-tail {
    font-family: "Barlow Condensed", sans-serif;
    font-weight: 700;
    font-size: 48px;
    line-height: 1;
    color: var(--title-grey);
    margin-top: 0;
  }
  .subtitle {
    font-family: "Barlow Condensed", sans-serif;
    font-weight: 600;
    font-size: 15px;
    letter-spacing: .3px;
    color: var(--paper-white);
    margin-top: 12px;
  }
  .genre {
    position: absolute; left: 0; right: 0; bottom: 40px;
    text-align: center;
    font-family: "Barlow Condensed", sans-serif;
    font-weight: 600;
    font-size: 13px;
    color: var(--paper-white);
  }

  .blurb {
    position: absolute; left: 50px; right: 50px; top: 178px;
    font-family: "Roboto Condensed", sans-serif;
    font-size: 12.5px;
    line-height: 1.62;
    text-align: center;
    color: var(--paper-white);
    text-shadow: 0 1px 3px rgba(0,0,0,.5);
  }
  .imprint-slot {
    position: absolute; left: 0; right: 0; bottom: 78px;
    text-align: center;
    font-family: "Roboto Condensed", sans-serif;
    font-size: 12.5px;
    line-height: 1.6;
    color: var(--paper-white);
  }

  .spine-text {
    position: absolute; left: 50%; top: 24px;
    transform-origin: 0 0;
    transform: rotate(90deg) translateY(-50%);
    white-space: nowrap;
    display: flex; align-items: baseline; gap: 14px;
    font-family: "Barlow Condensed", sans-serif;
    font-weight: 600;
    font-size: 14px;
    color: var(--paper-white);
  }
  .spine-text .lead { color: var(--signal-red); font-weight: 700; }
  .spine-text .script { font-family: "Kaushan Script", cursive; font-weight: 400; font-size: 17px; }
  .spine-text .small { font-size: 9px; }
</style>
</head>
<body>
  <main class="cover-wrap">
    <section class="panel back-cover">
      <div class="scene-art" role="img" aria-label="Dunkle Seelandschaft in Värmland mit hellem Wolkenhimmel, bewaldetem Hügel, Seeufer und einem umgedrehten Boot im Vordergrund"></div>
      <p class="blurb">Auf einer Insel in einem See im schwedischen Värmland werden die Leichen von zwei jungen Frauen gefunden; sie sind nackt und kunstvoll drapiert. Inspektor Nils Malmgren, der von seiner Frau betrogen worden ist, beginnt, in diesem Fall zu ermitteln. Zugleich wird auf einem Feld ganz in der Nähe des Fundorts ein bewusstloser Mann entdeckt, der ebenfalls vollkommen nackt ist. Gibt es einen Zusammenhang zwischen den beiden Taten? Als sich dann der nackte Mann als Liebhaber seiner Frau herausstellt, wird der Fall für Malmgren und dessen Kollegin Lena Bergqvist persönlicher, als ihnen lieb ist.</p>
      <p class="imprint-slot">Platz für Verlag<br>und ISBN</p>
    </section>

    <section class="panel spine">
      <div class="spine-text">
        <span>KERSTIN LUND</span>
        <span><span class="lead">WO</span> <span class="script">Schatten</span> RUHEN</span>
        <span class="small">INSPEKTOR MALMGRENS LETZTER TAG</span>
      </div>
    </section>

    <section class="panel front-cover">
      <div class="scene-art" role="img" aria-label="Nebliger See mit Birke und dunklem Wald vor einem Hügel unter hellem Wolkenhimmel, im Vordergrund eine im hohen Gras liegende Gestalt im Dunkel"></div>
      <p class="author">KERSTIN LUND</p>
      <div class="title-block">
        <h1>
          <span class="title-lead">WO</span>
          <span class="title-main">Schatten</span>
          <span class="title-tail">RUHEN</span>
        </h1>
        <p class="subtitle">INSPEKTOR MALMGRENS LETZTER TAG</p>
      </div>
      <p class="genre">KRIMINALROMAN</p>
    </section>
  </main>
</body>
</html>
```